Flyer für Lach- und Humorworkshops
Zielgruppe
Ich biete Lach- und Humorworkshops an für Unternehmen und Privatpersonen, für mehr Lebensfreude und Erfolg, ob privat oder im Business.
Aufgabenstellung
- DIN A6
- Textvorgabe im Word kann auch gekürzt werden, je nach Platz auf dem Flyer
- Schlagwörter wie 'Lachen' in der Schrift 'Licorice' so wie auf der Website

```html
<!DOCTYPE html>
<html lang="de">
<head>
<meta charset="utf-8">
<title>Lach-Workshop Flyer</title>
<link rel="stylesheet" href="https://fonts.googleapis.com/css2?family=Licorice&family=Poppins:wght@300;400;600&display=swap">
<style>
  :root {
    --canvas: #f2ebe8;
    --paper: #f5f4f3;
    --blush: #f1ebe8;
    --sand: #ece3da;
    --taupe: #c2b2a0;
    --ink: #141414;
    --text: #8b7f78;
    --text-strong: #7c7068;
    --gold: #b89c7c;
    --gold-light: #dcc7a6;
  }
  * { box-sizing: border-box; margin: 0; padding: 0; }
  html, body { width: 1200px; height: 1200px; overflow: hidden; }
  body {
    background: var(--canvas);
    font-family: "Poppins", sans-serif;
    font-weight: 300;
    color: var(--text);
    position: relative;
  }
  .page {
    position: absolute;
    top: 227px;
    width: 527px;
    height: 746px;
    background: var(--paper);
    overflow: hidden;
  }
  .page--front { left: 62px; }
  .page--back { left: 630px; }
  .abs { position: absolute; }
  .script { font-family: "Licorice", cursive; font-weight: 400; line-height: 1; }

  /* front */
  .hero-bg { left: 0; top: 0; width: 527px; height: 286px; background: var(--blush); }
  .hero-art {
    left: 0; top: 9px; width: 251px; height: 277px;
    background: radial-gradient(circle at 70% 45%, #d9e3e3 0 28%, transparent 29%),
                linear-gradient(135deg, #2f6f73 0%, #c9553e 35%, #e3b24a 65%, #3b5d5c 100%);
    opacity: .85;
  }
  .hero-question { left: 265px; top: 30px; font-size: 21.5px; font-weight: 400; color: var(--ink); line-height: 1.05; }
  .hero-word { left: 262px; top: 78px; font-size: 96px; color: var(--ink); }
  .hero-swoosh { left: 290px; top: 160px; }
  .hero-box {
    left: 265px; top: 205px; width: 247px; height: 106px;
    background: var(--taupe); border-radius: 10px;
    padding: 11px 14px 0 17px;
    font-size: 12.5px; font-weight: 400; color: var(--ink); line-height: 1.3;
  }
  .why-title { left: 25px; top: 302px; font-size: 38px; color: var(--ink); }
  .reason { display: flex; align-items: center; gap: 14px; font-size: 12.5px; line-height: 1.4; color: var(--text); }
  .reason svg { flex: none; }
  .workshop-band { left: 0; top: 483px; width: 527px; height: 263px; background: var(--sand); }
  .workshop-photo {
    left: 0; top: 472px; width: 233px; height: 274px;
    background: linear-gradient(180deg, #ebe1d6 0%, #d8c8b4 45%, #2d2a28 75%, #24211f 100%);
  }
  .workshop-title { left: 25px; top: 497px; color: var(--ink); }
  .workshop-title .script { font-size: 44px; display: block; }
  .workshop-title .sub { font-size: 19px; font-weight: 400; display: block; margin-top: -6px; }
  .workshop-lead { left: 248px; top: 506px; width: 270px; font-size: 13px; font-weight: 600; color: var(--text-strong); line-height: 1.34; }
  .workshop-body { left: 248px; top: 605px; width: 272px; font-size: 13px; line-height: 1.38; color: var(--text); }

  /* back */
  .biz-title { left: 19px; top: 20px; font-size: 40px; color: var(--gold); }
  .biz-sub { left: 19px; top: 56px; font-size: 19px; font-weight: 400; color: var(--text-strong); }
  .biz-text { left: 19px; top: 95px; width: 490px; font-size: 12.4px; line-height: 1.34; color: var(--text); }
  .topics-band { left: 0; top: 265px; width: 527px; height: 154px; background: var(--sand); }
  .topics-lead { left: 20px; top: 283px; width: 480px; font-size: 13px; font-weight: 600; color: var(--text-strong); line-height: 1.35; }
  .topics { list-style: none; font-size: 13.5px; line-height: 1.62; color: var(--text); }
  .topics li::before { content: "• "; }
  .about-photo {
    left: 0; top: 431px; width: 171px; height: 304px;
    background: linear-gradient(180deg, #f1ece3 0%, #e3d3bd 40%, #bfa488 62%, #2e2b29 82%, #262321 100%);
  }
  .about-kicker { left: 201px; top: 433px; font-size: 12.5px; color: var(--text); }
  .about-name { left: 199px; top: 452px; font-size: 58px; color: var(--gold); }
  .about-claim { left: 201px; top: 508px; font-size: 13.3px; font-weight: 400; color: var(--ink); }
  .about-text { left: 201px; top: 535px; width: 300px; font-size: 12px; line-height: 1.25; color: var(--text); }
  .about-rule { left: 201px; top: 648px; width: 296px; height: 1px; background: #9c918a; }
  .brand { left: 201px; top: 670px; display: flex; align-items: center; gap: 8px; font-size: 34px; font-weight: 300; color: var(--gold); }
  .brand-dot { width: 10px; height: 10px; border-radius: 50%; background: var(--gold); }
  .contact { left: 365px; top: 666px; font-size: 13px; line-height: 1.27; color: var(--text-strong); }
  .contact strong { font-weight: 600; }
  .gold-bar { left: 0; top: 735px; width: 527px; height: 11px; background: linear-gradient(90deg, #c7a57c, #f0dfbe 45%, #b7925f 75%, #e6cfa7); }
</style>
</head>
<body>

<section class="page page--front">
  <div class="abs hero-bg"></div>
  <div class="abs hero-art" role="img" aria-label="Gemälde einer lachenden Frau mit Blumen im Haar und einem Tukan"></div>
  <h1 class="abs hero-question">Wann hast du das<br>letzte Mal so richtig</h1>
  <div class="abs script hero-word">gelacht?</div>
  <svg class="abs hero-swoosh" width="220" height="30" viewBox="0 0 220 30"><path d="M4 24 C70 18 140 12 216 6" stroke="#e0d4c8" stroke-width="1.5" fill="none"/></svg>
  <p class="abs hero-box">Lachen ist nicht nur ein Ausdruck von Freude, es ist gesund für unseren Körper, ausgleichend für unseren Geist und Balsam für unsere Seele.</p>

  <h2 class="abs script why-title">Warum lachen?</h2>
  <div class="abs reason" style="left:22px;top:360px">
    <svg width="38" height="34" viewBox="0 0 38 34" fill="none" stroke="#c2a98e" stroke-width="1.3"><path d="M19 13 C14 8 9 11 12 15 L19 20 L26 15 C29 11 24 8 19 13Z"/><path d="M3 10 L6 24 L14 31 M35 10 L32 24 L24 31"/></svg>
    <span>Lachen ist einfach, gesund<br>und macht glücklich.</span>
  </div>
  <div class="abs reason" style="left:284px;top:360px">
    <svg width="30" height="30" viewBox="0 0 30 30" fill="none" stroke="#c2a98e" stroke-width="1.3"><circle cx="14" cy="14" r="12"/><circle cx="14" cy="14" r="7"/><path d="M2 14 H26 M14 2 V26"/><path d="M22 24 L27 28"/></svg>
    <span>Lachen ist eine universelle<br>Sprache, die verbindet.</span>
  </div>
  <div class="abs reason" style="left:22px;top:413px">
    <svg width="42" height="32" viewBox="0 0 42 32" fill="none" stroke="#c2a98e" stroke-width="1.3"><circle cx="14" cy="19" r="11"/><circle cx="28" cy="19" r="11"/><path d="M9 21 Q14 26 19 21 M23 21 Q28 26 33 21"/><path d="M21 2 V5 M15 4 L17 7 M27 4 L25 7"/></svg>
    <span>Lachen ist sofort wirksam<br>und nachhaltig zugleich.</span>
  </div>
  <div class="abs reason" style="left:284px;top:413px">
    <svg width="34" height="34" viewBox="0 0 34 34" fill="none" stroke="#c2a98e" stroke-width="1.3"><path d="M17 4 C13 9 13 14 17 18 C21 14 21 9 17 4Z M17 18 C11 17 8 12 8 9 C12 10 15 13 17 18 M17 18 C23 17 26 12 26 9 C22 10 19 13 17 18"/><path d="M2 27 C8 23 14 24 19 26 L30 22 M2 31 L10 30 L22 30 L32 24"/></svg>
    <span>Lachen ist ganzheitlich,<br>nachhaltig und sinnvoll.</span>
  </div>

  <div class="abs workshop-band"></div>
  <div class="abs workshop-photo" role="img" aria-label="Foto der Lach-Trainerin, lachend im schwarzen T-Shirt mit Aufschrift"></div>
  <h2 class="abs workshop-title"><span class="script">Lach-</span><span class="sub">Workshop</span></h2>
  <p class="abs workshop-lead">Du suchst eine besondere Teambuilding Aktivität? Wie wäre es mit einer kurzen Auszeit aus dem Alltag, die lustig, gesund, nachhaltig und sinnvoll ist?</p>
  <p class="abs workshop-body">In einem Lach-Workshop geht es in erster Linie darum, gemeinsam Spass zu haben und ausgiebig zu lachen. Euch erwartet ein abwechslungsreicher Mix aus einfachen, spielerischen und kreativen Übungen.</p>
</section>

<section class="page page--back">
  <h2 class="abs script biz-title">Humor im Business –</h2>
  <p class="abs biz-sub">für ein positives Betriebsklima</p>
  <p class="abs biz-text">Lachen ist gesund – das gilt nicht nur für unsere persönliche Gesundheit, sondern auch für ein Unternehmen. Lachen ist eine universelle, positive Form der Kommunikation. Lachen ist essentiell für zwischenmenschliche Beziehungen, denn Lachen schafft Vertrauen und Nähe. Wo gelacht wird, fühlen wir uns wohl, der Teamgeist wird gestärkt, Kreativität und Leistungsbereitschaft werden gefördert. Gesunde, zufriedene, motivierte und ausgeglichene Mitarbeitende lösen Herausforderungen viel kreativer und effizienter. Denn nur wer Freude hat bei der Arbeit, ist zu dauerhaften Höchstleistungen fähig.</p>

  <div class="abs topics-band"></div>
  <p class="abs topics-lead">Lachen &amp; Humor lässt sich sehr vielseitig integrieren, kann einen Anlass bereichern oder ergänzen:</p>
  <ul class="abs topics" style="left:20px;top:334px">
    <li>Teambuilding</li>
    <li>Persönlichkeitsentwicklung</li>
    <li>Stressmanagement</li>
  </ul>
  <ul class="abs topics" style="left:271px;top:334px">
    <li>Gesundheit &amp; Wohlbefinden</li>
    <li>Kreaktivität &amp; Innovation</li>
  </ul>

  <div class="abs about-photo" role="img" aria-label="Porträtfoto der Lach-Trainerin vor goldenem Farbspritzer"></div>
  <p class="abs about-kicker">Über mich:</p>
  <h2 class="abs script about-name">Ich bin Selina</h2>
  <p class="abs about-claim">Natürlich. Empathisch. Professionell.</p>
  <p class="abs about-text">Ich lache fürs Leben gerne! Als Lach-Trainerin habe ich es mir zur Aufgabe gemacht, Menschen mit Lachen &amp; Humor zu inspirieren. Mein persönliches Ziel ist es, mehr Vitalität und Zufriedenheit in den Alltag möglichst vieler Menschen zu bringen, mit etwas, das so einfach, natürlich und alltäglich ist: LACHEN.</p>
  <div class="abs about-rule"></div>
  <div class="abs brand"><span class="brand-dot"></span>lumea</div>
  <p class="abs contact"><strong>Selina Aebischer</strong><br>www.lumea-lachen.ch<br>hallo@lumea-lachen.ch<br>+41 79 000 12 34</p>
  <div class="abs gold-bar"></div>
</section>

</body>
</html>
```